Prepared ready to cook meal delivery service needs a flyer design

We need a flyer design for a startup company based in Cape Town, South Africa. I've attached a few flyer designs that I like.

The company is called 'Brindle' and our website will be found at brindle.co.za. We don't have a logo yet.

Flyer text:

Brindle
Ready to roast

Do you feel like a home cooked meal but don't like shopping, peeling, chopping, cooking, or cleaning up?

We deliver ready to roast free range chicken and fresh vegetables to your door.

To order: SMS your name to 083 614 2958 and we'll call you back.

Only the best ingredients used
Free range chickens. Fresh herbs and vegetables. Virgin olive oil.

No bad carbs!

Ready to roast Free range chicken and fresh veggies
For 2 R99
For 4 R139
Updates

Wording of flyer updated.

Target Market(s)

Local Cape Townians that hate grocery shopping and need help saving time preparing meals.

Industry/Entity Type

Delivery Service

Requirements
Must have
• To find out more: SMS your name to 083 614 2958

```html
<!DOCTYPE html>
<html lang="en">
<head>
<meta charset="utf-8">
<title>Brindle – ready to roast flyers</title>
<link rel="stylesheet" href="https://fonts.googleapis.com/css2?family=Alfa+Slab+One&family=Quicksand:wght@400&display=swap">
<style>
  :root {
    --board: #a6a6a6;
    --brown: #5b3518;
    --brown-deep: #3d2210;
    --white: #ffffff;
    --sky-top: #1cbdf0;
    --sky-low: #c9ecfa;
    --green: #8cc63f;
    --blue: #1f70b6;
    --navy: #2b2d6a;
    --red: #e8222e;
    --rule: #ffffff;
  }
  * { box-sizing: border-box; margin: 0; padding: 0; }
  html, body {
    width: 1200px; height: 832px; overflow: hidden;
    background: var(--board);
  }
  body { position: relative; font-family: "Quicksand", sans-serif; font-weight: 400; }
  h1, h2, p { font-weight: 400; white-space: nowrap; }

  .flyer { position: absolute; overflow: hidden; }

  /* ---------- brown flyer ---------- */
  .flyer--brown {
    left: 7px; top: 7px; width: 579px; height: 817px;
    background: var(--brown); color: var(--white);
  }
  .flyer--brown .band {
    position: absolute; left: 0; right: 0; top: 106px; height: 127px;
    background: var(--white);
  }
  .price-tag {
    position: absolute; top: 150px; width: 140px; margin-left: -70px;
    text-align: center; color: var(--brown-deep);
    font-size: 23px; line-height: 32px;
  }
  .price-tag--two { left: 66px; }
  .price-tag--four { left: 513px; }
  .brand-badge {
    position: absolute; left: 289px; top: 161px;
    width: 270px; height: 270px; margin: -135px 0 0 -135px;
    border-radius: 50%; background: var(--brown-deep);
    border: 12px solid var(--white);
    display: flex; align-items: center; justify-content: center;
  }
  .brand-badge__name { font-size: 44px; color: var(--white); letter-spacing: 3px; }

  .centered { position: absolute; left: 0; right: 0; text-align: center; }
  .pitch { top: 332px; font-size: 28px; line-height: 44px; }
  .divider { position: absolute; left: 57px; width: 464px; border: 0; }
  .divider--solid { top: 476px; border-top: 2px solid var(--rule); }
  .divider--dotted { border-top: 2px dotted var(--rule); opacity: .85; }
  .note { font-size: 19px; line-height: 28px; }
  .note--long { font-size: 17.5px; }
  .order { font-size: 22px; line-height: 32px; }

  /* ---------- sky flyer ---------- */
  .flyer--sky {
    left: 613px; top: 6px; width: 577px; height: 818px;
    background: linear-gradient(180deg, var(--sky-top) 0%, #7fd6f6 30%, var(--sky-low) 55%, var(--white) 100%);
    border: 1px solid #8c8c8c;
  }
  .title {
    position: absolute; left: 0; right: 0; top: 22px; text-align: center;
    font-family: "Alfa Slab One", serif; font-size: 82px; line-height: 90px;
    color: var(--blue); letter-spacing: 2px;
  }
  .tagline {
    position: absolute; left: 0; right: 0; top: 105px; text-align: center;
    font-size: 44px; line-height: 54px; color: var(--navy);
  }
  .question-shadow, .question {
    position: absolute; width: 490px; height: 140px;
    border-radius: 75px 0 0 75px;
  }
  .question-shadow { left: 94px; top: 178px; background: rgba(255,255,255,.75); }
  .question {
    left: 101px; top: 165px; background: var(--green); color: var(--white);
    display: flex; align-items: center; justify-content: center; text-align: center;
    font-size: 22px; line-height: 35px; padding-left: 8px;
  }
  .promise { top: 322px; color: var(--white); font-size: 24px; line-height: 35px; }
  .dish-photo {
    position: absolute; left: 8px; top: 398px; width: 552px; height: 420px;
    border-radius: 16px 16px 0 0;
    background:
      radial-gradient(ellipse 48% 42% at 50% 40%, #d9a24e 0%, #b97a30 55%, transparent 75%),
      linear-gradient(180deg, #f4f1ec 0%, #8a4a3a 30%, #6c7a35 60%, #c2452f 100%);
  }
  .info-panel {
    position: absolute; left: 0; top: 662px; width: 536px; height: 83px;
    background: var(--white); color: var(--green);
    text-align: center; font-size: 16.5px; line-height: 26px; padding-top: 2px;
  }
  .order-bar {
    position: absolute; left: 0; top: 745px; width: 536px; height: 62px;
    background: var(--green); color: var(--white); border-radius: 0 0 40px 0;
    text-align: center; font-size: 19px; line-height: 27px; padding-top: 4px;
  }
  .price-badge {
    position: absolute; left: 414px; top: 533px; width: 132px; height: 132px;
    border-radius: 50%; background: var(--red); color: var(--white);
    display: flex; flex-direction: column; align-items: center; justify-content: center;
    text-align: center;
  }
  .price-badge__label { font-size: 19px; line-height: 24px; }
  .price-badge__amount { font-size: 28px; line-height: 34px; }
</style>
</head>
<body>

<section class="flyer flyer--brown">
  <div class="band"></div>
  <p class="price-tag price-tag--two">Meal for 2<br>R99</p>
  <p class="price-tag price-tag--four">Meal for 4<br>R139</p>
  <div class="brand-badge"><span class="brand-badge__name">Brindle</span></div>

  <h2 class="centered pitch">Do you feel like a home cooked meal but<br>don't like shopping, peeling, chopping,<br>cooking, or cleaning up?</h2>
  <hr class="divider divider--solid">

  <p class="centered note" style="top:497px">We deliver ready to roast free range chicken<br>and fresh vegetables to your door.</p>
  <hr class="divider divider--dotted" style="top:566px">
  <p class="centered note" style="top:580px">Only the best ingredients used!</p>
  <hr class="divider divider--dotted" style="top:622px">
  <p class="centered note note--long" style="top:636px">Free range chickens. Fresh herbs and vegetables. Virgin olive oil.</p>
  <hr class="divider divider--dotted" style="top:675px">
  <p class="centered note" style="top:691px">No bad carbs!</p>
  <hr class="divider divider--dotted" style="top:728px">
  <p class="centered order" style="top:740px">To order: SMS your name to 083 614 2958<br>and we'll call you back.</p>
</section>

<section class="flyer flyer--sky">
  <h1 class="title">BRINDLE</h1>
  <p class="tagline">ready to roast</p>
  <div class="question-shadow"></div>
  <p class="question">Do you feel like a home cooked meal<br>but don't like shopping, peeling, chopping,<br>cooking, or cleaning up?</p>
  <p class="centered promise">We deliver ready to roast free range chicken<br>and fresh vegetables to your door.</p>

  <div class="dish-photo" role="img" aria-label="Golden roast chicken on roasted vegetables in a white dish"></div>

  <div class="info-panel">
    <p>Only the best ingredients used!</p>
    <p>Free range chickens. Fresh herbs and vegetables. Virgin olive oil.</p>
    <p>No bad carbs!</p>
  </div>
  <div class="order-bar">
    <p>To order: SMS your name to 083 614 2958</p>
    <p>and we'll call you back.</p>
  </div>

  <div class="price-badge">
    <span class="price-badge__label">Meal for 2</span>
    <span class="price-badge__amount">R99</span>
    <span class="price-badge__label">Meal for 4</span>
    <span class="price-badge__amount">R139</span>
  </div>
</section>

</body>
</html>
```